FACEBOOK PAGE FOR BREVLO PLUMBING GROUP

We need a facebook banner for our new plumbing business.

Needs to be catchy and inline with our logo.

Phone: 0472 836 291
Email: hello@brevlo.com.au
website: www.brevlo.com.au
Servicing: Perth Metro Areas and surrounding suburbs
Services:
*We offer a wide range of services, including:
Plumbing – General maintenance, blocked drains, toilet repairs, burst pipes, reticulation, renovations & emergencies.

*Hot Water – Installation, servicing & repairs for all systems.

*Cooling & Heating – Air conditioning, evaporative cooling & heater servicing.

*Filtration – Filtered taps, under-sink systems & whole-house filtration setups.

Our Mission

Brevlo Group believes plumbing shouldn't break the bank - or your trust. Our mission is to provide honest, affordable, and no-nonsense plumbing services that get the job done right the first time. No runaround - just reliable work, and the respect every customer deserves.

What Makes Us Different???

Upfront Fixed Pricing
No surprises, no hidden fees. You get clear, honest quotes before any work begins.

Respectful, Customer-First Service
We show up on time, communicate clearly, and treat your property like it’s our own.

Locals Serving Locals
We’re proud to support the Perth community with reliable, high-quality plumbing backed by real local care.

FOR THE DESIGNER A little background on us as a new biz for your reference:
By Locals, For Locals
After 13 years in the plumbing industry, seasoned local plumber Wade founded his company to address the widespread issue of homeowners and businesses being overcharged or receiving inferior work. He knew there had to be a better way—and that’s when Brevlo was created.
Today, Brevlo Group is a trusted plumbing company based in Osborne Park, proudly serving residential, commercial, and industrial clients across the Perth metro area. With over a decade of experience, we deliver expert workmanship, fair pricing, and treat every job—big or small—with the same care and professionalism.
Need it done right—and affordably? Get it sorted with BREVLO now!

```html
<!DOCTYPE html>
<html lang="en">
<head>
<meta charset="utf-8">
<title>Brevlo Plumbing Group – Facebook Cover</title>
<link href="https://fonts.googleapis.com/css2?family=Montserrat:wght@500;600;700;800&display=swap" rel="stylesheet">
<style>
  :root {
    --navy: #1c3a7e;
    --navy-deep: #1a2f6b;
    --cyan: #0aa8e6;
    --white: #ffffff;
    --page: #ffffff;
    --photo-top: #c9d6ef;
    --photo-mid: #2f55c8;
    --photo-low: #223f9f;
  }
  * { margin: 0; padding: 0; box-sizing: border-box; }
  html, body { width: 1200px; height: 853px; overflow: hidden; background: var(--page); }
  body { font-family: "Montserrat", sans-serif; position: relative; }

  .cover {
    position: absolute; left: 20px; top: 211px;
    width: 1160px; height: 430px;
    overflow: hidden; background: #f7f7f8;
  }
  .cover-art { position: absolute; inset: 0; }

  .headline {
    position: absolute; left: 76px; top: 50px;
    font-weight: 800; font-size: 41px; line-height: 46px; letter-spacing: -0.3px;
  }
  .headline .line-1 { color: var(--navy); display: block; }
  .headline .line-2 { color: var(--cyan); display: block; }

  .brand {
    position: absolute; left: 572px; top: 40px;
    display: flex; align-items: center; gap: 10px;
  }
  .brand-mark { width: 20px; height: 20px; border-radius: 50%; background: var(--cyan); }
  .brand-name { font-weight: 700; font-size: 36px; letter-spacing: 9px; color: var(--navy-deep); }

  .promise {
    position: absolute; left: 612px; top: 124px; color: var(--white);
    font-weight: 700; font-size: 16px; line-height: 19px;
  }
  .promise .rule { width: 190px; height: 1px; background: rgba(255,255,255,0.55); margin: 6px 0 7px; }

  .services {
    position: absolute; left: 41px; top: 178px; width: 560px;
    color: var(--white); font-weight: 500; font-size: 12.6px; line-height: 16.5px;
    list-style: none;
  }
  .services li { margin-bottom: 5px; }
  .services .label { color: var(--cyan); font-weight: 600; }

  .contacts {
    position: absolute; left: 49px; top: 311px;
    display: flex; align-items: center;
  }
  .contact { display: flex; align-items: center; gap: 6px; color: var(--navy); font-weight: 700; font-size: 17.5px; }
  .contact.phone { margin-right: 22px; }
  .contact.email { margin-right: 25px; }
  .contact-icon { width: 26px; height: 26px; border-radius: 4px; background: var(--cyan); display: flex; align-items: center; justify-content: center; }

  .tagline {
    position: absolute; left: 228px; top: 355px; height: 20px;
    font-weight: 800; font-size: 9.2px; line-height: 20px; text-transform: uppercase; white-space: nowrap;
  }
  .tagline .ask { color: var(--cyan); margin-right: 8px; }
  .tagline .call { color: var(--white); }

  .hero-photo {
    position: absolute; left: 830px; top: 0; width: 210px; height: 430px;
    background: linear-gradient(180deg, var(--photo-top) 0%, var(--photo-mid) 45%, var(--photo-low) 100%);
  }
</style>
</head>
<body>
  <section class="cover" aria-label="Brevlo Plumbing Group Facebook cover">
    <svg class="cover-art" width="1160" height="430" viewBox="0 0 1160 430" aria-hidden="true">
      <defs>
        <linearGradient id="facet" x1="0" y1="0" x2="1" y2="0">
          <stop offset="0" stop-color="#e2e3e6"/>
          <stop offset="1" stop-color="#f7f7f8"/>
        </linearGradient>
        <linearGradient id="wave" x1="0" y1="0" x2="0.4" y2="1">
          <stop offset="0" stop-color="#1d3f8a"/>
          <stop offset="0.5" stop-color="#1380c6"/>
          <stop offset="1" stop-color="#08aeea"/>
        </linearGradient>
        <linearGradient id="promiseFill" x1="0" y1="0" x2="1" y2="0">
          <stop offset="0" stop-color="#12a8e6"/>
          <stop offset="1" stop-color="#1c3a7e"/>
        </linearGradient>
      </defs>

      <polygon points="0,0 110,0 0,180" fill="#e4e5e8"/>
      <polygon points="110,0 338,0 170,280 0,280 0,180" fill="url(#facet)"/>
      <polygon points="338,0 570,0 454,190" fill="#f1f2f4" opacity="0.8"/>
      <polygon points="0,395 340,395 318,430 0,430" fill="#e9eaec"/>
      <polygon points="110,395 340,395 318,430 90,430" fill="url(#facet)"/>
      <polygon points="0,295 110,295 0,380" fill="#ececee"/>

      <path d="M958,0 H1160 V430 H860 V130 C905,100 935,40 958,0 Z" fill="url(#wave)"/>
      <path d="M860,131 C950,118 1060,112 1160,112 V148 C1060,150 960,168 860,182 Z" fill="#ffffff"/>
      <path d="M860,248 C960,250 1070,250 1160,238 V266 C1060,282 960,300 860,318 Z" fill="#ffffff"/>
      <polygon points="1132,0 1160,0 1160,38" fill="#ffffff"/>

      <polygon points="0,168 512,168 482,222 830,222 830,295 0,295" fill="var(--navy)"/>
      <polygon points="527,113 830,113 830,222 482,222" fill="#ffffff"/>
      <polygon points="541,120 830,120 830,215 497,215" fill="url(#promiseFill)"/>

      <g fill="none" stroke="#ffffff" stroke-width="2" stroke-linecap="round" stroke-linejoin="round">
        <circle cx="572" cy="170" r="21"/>
        <circle cx="572" cy="170" r="15"/>
        <path d="M565,170 l5,5 l9,-10"/>
        <path d="M568,145 h8 M572,145 v4"/>
        <path d="M540,162 h12 M537,170 h10 M540,178 h12"/>
      </g>

      <line x1="640" y1="362" x2="760" y2="362" stroke="var(--navy)" stroke-width="1"/>
      <polygon points="219,346 656,346 648,376 210,376" fill="var(--navy)"/>
    </svg>

    <h1 class="headline">
      <span class="line-1">Expert Plumbers,</span>
      <span class="line-2">24 Hours a Day</span>
    </h1>

    <div class="brand">
      <span class="brand-name">BREVLO</span>
      <span class="brand-mark"></span>
    </div>

    <div class="promise">
      <p>Guaranteed Fast,<br>Reliable services</p>
      <div class="rule"></div>
      <p>No surprises,<br>no hidden fees.</p>
    </div>

    <ul class="services">
      <li><span class="label">PLUMBING</span> – General maintenance, blocked drains, toilet repairs,<br>burst pipes, reticulation, renovations &amp; emergencies.</li>
      <li><span class="label">HOT WATER</span> – Installation, servicing &amp; repairs for all systems.</li>
      <li><span class="label">COOLING &amp; HEATING</span> – Air conditioning, evaporative cooling &amp; heater servicing.</li>
      <li><span class="label">FILTRATION</span> – Filtered taps, under-sink systems &amp; whole-house filtration setups.</li>
    </ul>

    <div class="contacts">
      <div class="contact phone">
        <span class="contact-icon">
          <svg width="16" height="16" viewBox="0 0 24 24" fill="none" stroke="#fff" stroke-width="2" stroke-linejoin="round"><path d="M5 3h4l2 5-3 2a12 12 0 0 0 6 6l2-3 5 2v4a2 2 0 0 1-2 2A17 17 0 0 1 3 5a2 2 0 0 1 2-2z"/></svg>
        </span>
        0472 836 291
      </div>
      <div class="contact email">
        <span class="contact-icon">
          <svg width="16" height="16" viewBox="0 0 24 24" fill="none" stroke="#fff" stroke-width="2" stroke-linecap="round"><path d="M10 14a4 4 0 0 0 6 0l3-3a4 4 0 0 0-6-6l-1 1"/><path d="M14 10a4 4 0 0 0-6 0l-3 3a4 4 0 0 0 6 6l1-1"/></svg>
        </span>
        hello@brevlo.com.au
      </div>
      <div class="contact web">
        <span class="contact-icon">
          <svg width="16" height="16" viewBox="0 0 24 24" fill="none" stroke="#fff" stroke-width="2"><circle cx="12" cy="12" r="9"/><path d="M3 12h18M12 3c3 3 3 15 0 18M12 3c-3 3-3 15 0 18"/></svg>
        </span>
        www.brevlo.com.au
      </div>
    </div>

    <p class="tagline"><span class="ask">Need it done right and affordably?</span><span class="call">Get it sorted with BREVLO now!</span></p>

    <div class="hero-photo" role="img" aria-label="Photo of a smiling plumber in a blue polo and overalls giving a thumbs up and holding a red pipe wrench"></div>
  </section>
</body>
</html>
```